Book Cover for Senior Care Agencies

Design a cover [kindle and print] for a book of interviews with home health care agencies, that also has client stories [like a Lantern Pages for the Weary type book]

The title is
Hands That Stay

subtitle
Picking A Fitting Elder Support Service

The book will have 7 co-authors, so they will need to be listed on the cover
Print book Size 6 x 9

For image, I like the idea of an adult helping their senior parent out... What i am going for is very, clean and crisp yet warm. No cartoons.

I don't tend to like script fonts.
thank you

Target Market(s)

Family members who have senior relatives or parents

Industry/Entity Type

Health Care

Font styles to use
Serif
Sans Serif

Requirements
Should not have
• cartoons

```html
<!DOCTYPE html>
<html lang="en">
<head>
<meta charset="utf-8">
<title>Hands That Stay – Cover Spread</title>
<link rel="stylesheet" href="https://fonts.googleapis.com/css2?family=Cinzel:wght@400&family=Cinzel+Decorative:wght@400&family=Source+Sans+3:wght@400&display=swap">
<style>
  :root {
    --paper: #ffffff;
    --edge: #c8c8c8;
    --trim: #8a8a8a;
    --ink: #141414;
    --title-light: #ffffff;
    --back-dark: #4a5052;
    --back-mid: #8e9492;
    --back-light: #d6d8d2;
    --gold-dark: #3c2a14;
    --gold-mid: #a8803e;
    --gold-light: #e9cf98;
  }
  html, body {
    margin: 0;
    padding: 0;
    overflow: hidden;
    background: var(--paper);
  }
  .canvas {
    position: relative;
    width: 1200px;
    height: 1000px;
    box-sizing: border-box;
    border: 1px solid var(--edge);
    background: var(--paper);
    overflow: hidden;
  }
  .panel {
    position: absolute;
    top: 113px;
    height: 774px;
  }
  .back-cover {
    left: 55px;
    width: 516px;
    background:
      radial-gradient(ellipse 210px 260px at 420px 380px, var(--back-light) 0%, rgba(214,216,210,0) 100%),
      radial-gradient(ellipse 160px 160px at 440px 660px, rgba(40,44,46,0.8) 0%, rgba(40,44,46,0) 100%),
      linear-gradient(180deg, var(--back-dark) 0%, var(--back-mid) 45%, #7d8382 100%);
  }
  .spine {
    left: 571px;
    width: 58px;
    background: linear-gradient(180deg, #3e3222 0%, #6d5631 45%, #5d4524 100%);
  }
  .front-cover {
    left: 629px;
    width: 516px;
    background:
      radial-gradient(ellipse 230px 240px at 180px 400px, var(--gold-light) 0%, rgba(233,207,152,0) 100%),
      radial-gradient(ellipse 120px 160px at 120px 700px, rgba(30,20,10,0.85) 0%, rgba(30,20,10,0) 100%),
      radial-gradient(ellipse 80px 80px at 200px 40px, rgba(20,14,8,0.8) 0%, rgba(20,14,8,0) 100%),
      linear-gradient(90deg, #6a4f28 0%, var(--gold-mid) 40%, #d7b06a 75%, #9c7236 100%);
  }
  .trim-line {
    position: absolute;
    top: 97px;
    width: 1px;
    height: 806px;
    background: var(--trim);
  }
  .trim-line--left { left: 571px; }
  .trim-line--right { left: 628px; }

  .back-title {
    position: absolute;
    left: 0;
    top: 52px;
    width: 284px;
    margin: 0;
    text-align: center;
    font-family: "Cinzel Decorative", serif;
    font-weight: 400;
    font-size: 38px;
    line-height: 43px;
    color: var(--title-light);
  }
  .back-subtitle {
    position: absolute;
    left: 0;
    top: 146px;
    width: 284px;
    margin: 0;
    text-align: center;
    font-family: "Cinzel", serif;
    font-size: 16px;
    line-height: 21px;
    color: var(--ink);
  }
  .back-blurb {
    position: absolute;
    left: 45px;
    top: 208px;
    width: 218px;
    font-family: "Source Sans 3", sans-serif;
    font-size: 13.5px;
    line-height: 24px;
    color: var(--ink);
    text-align: justify;
  }
  .back-blurb p { margin: 0 0 24px; }

  .spine-text {
    position: absolute;
    left: 0;
    top: 36px;
    width: 58px;
    height: 710px;
    writing-mode: vertical-rl;
    display: flex;
    align-items: center;
    white-space: nowrap;
    color: var(--title-light);
  }
  .spine-title {
    font-family: "Cinzel Decorative", serif;
    font-size: 23px;
    margin-bottom: 14px;
  }
  .spine-subtitle {
    font-family: "Cinzel", serif;
    font-size: 14.5px;
    letter-spacing: 0.3px;
  }

  .front-title {
    position: absolute;
    left: 175px;
    top: 60px;
    width: 330px;
    margin: 0;
    text-align: center;
    font-family: "Cinzel Decorative", serif;
    font-weight: 400;
    font-size: 76px;
    line-height: 90px;
    color: var(--title-light);
  }
  .front-subtitle {
    position: absolute;
    left: 195px;
    top: 556px;
    width: 300px;
    margin: 0;
    text-align: center;
    font-family: "Cinzel", serif;
    font-size: 31px;
    line-height: 40px;
    color: var(--ink);
  }
</style>
</head>
<body>
<div class="canvas">
  <section class="panel back-cover" role="img" aria-label="Soft-focus photograph of an open hand reaching forward, in cool grey tones">
    <h2 class="back-title">Hands That<br>Stay</h2>
    <p class="back-subtitle">PICKING A FITTING<br>ELDER SUPPORT SERVICE</p>
    <div class="back-blurb">
      <p>Lorem ipsum dolor sit amet, consectetuer hutyu adipiscing elit. Aenean commodo ligula eget no dolor. Aenean massa. Cum sociis natoque nulla penatibus et magnis dis parturient montes, nascetur ridiculus mus. Donec quam felis, ultricies loput nec, pellentesque eu, pretium quis, sem. Nulla consequat massa quis enim. Donec pede justo,</p>
      <p>In enim justo, rhoncus ut, imperdiet a, venenatis vitae, justo. Nullam dictum felis eu pede mollis pretium. Integer tincidunt. Cras dapibus. Vivamus elementum semper nisi. Aenean vulputate eleifend tellus. Aenean leo ligula, porttitor eu, consequat vitae,</p>
    </div>
  </section>

  <section class="panel spine">
    <div class="spine-text">
      <span class="spine-title">Hands That Stay</span>
      <span class="spine-subtitle">PICKING A FITTING ELDER SUPPORT SERVICE</span>
    </div>
  </section>

  <section class="panel front-cover" role="img" aria-label="Soft-focus photograph of an open hand reaching forward, in warm golden tones">
    <h1 class="front-title">Hands<br>That<br>Stay</h1>
    <p class="front-subtitle">PICKING A<br>FITTING ELDER<br>SUPPORT<br>SERVICE</p>
  </section>

  <div class="trim-line trim-line--left"></div>
  <div class="trim-line trim-line--right"></div>
</div>
</body>
</html>
```